Business Card Design Project for Electrical Company

We need a business card designed for a new Electrical Company called Dorvel Electrical Solutions, i dont mind if only Dorvel Electrical is used. We are a domestic and commercial Electrical Company that provides a range of Electrical Services. Our Company colours are Fluro Yellow and Black with the Lightning bolt picture attached.I have attached a card that has been made i think it is rather basic and am looking for something more. the font of Dorvel Electrical has been used on our car graphics as well as the lightning bolt. i want to keep them the same so we can brand our business. Some things we want on the front of the card are Dorvel Electrical Solutions, Owen Platt, 0438516274, admin@dorvelelectrical.example, Lic No 58342, Servicing CQ Region. But we want Owens name seperate to the phone number as its the phone number for the office, owen wont be answering the phone so we are thinking we dont want to give that impression. What do you think? with all that if you have complete different font designs please submit what you think would work best. keeping in mind our company name and details as well as coulors.

Industry/Entity Type

Business

```html
<!DOCTYPE html>
<html lang="en">
<head>
<meta charset="utf-8">
<title>Dorvel Electrical Solutions – Business Card</title>
<link rel="stylesheet" href="https://fonts.googleapis.com/css2?family=Cinzel:wght@400;700&family=Roboto+Condensed:wght@700&family=Kaushan+Script&family=Oswald:wght@700&display=swap">
<style>
  :root {
    --stage: #3b4049;
    --card-black: #050505;
    --fluro: #d2f20c;
    --white: #ffffff;
    --ink: #0a0a0a;
    --muted-olive: #a9ad86;
    --label: #bfcde2;
    --strip: rgba(0, 0, 0, 0.62);
  }
  * { margin: 0; padding: 0; box-sizing: border-box; }
  html, body { width: 1000px; height: 1200px; overflow: hidden; }
  body { background: var(--stage); position: relative; font-family: "Cinzel", serif; }

  .card {
    position: absolute;
    left: 194px;
    width: 586px;
    height: 351px;
    background: var(--card-black);
    overflow: hidden;
    box-shadow: 0 6px 18px rgba(0,0,0,0.45);
  }
  .card--front { top: 150px; }
  .card--back { top: 617px; }

  .card-art { position: absolute; inset: 0; }

  /* Front */
  .brand {
    position: absolute;
    left: 66px;
    top: 62px;
    display: flex;
    align-items: center;
    gap: 14px;
  }
  .brand-dot {
    width: 22px; height: 22px;
    border-radius: 50%;
    background: var(--fluro);
    flex: none;
  }
  .brand-name {
    color: var(--white);
    font-family: "Roboto Condensed", sans-serif;
    font-weight: 700;
    font-size: 34px;
    line-height: 1.1;
  }

  .name-band {
    position: absolute;
    left: 0; top: 199px;
    width: 246px; height: 34px;
    background: var(--fluro);
  }
  .person-name {
    position: absolute;
    left: 66px; top: 199px;
    height: 34px; line-height: 34px;
    font-family: "Roboto Condensed", sans-serif;
    font-weight: 700;
    font-size: 33px;
    color: var(--ink);
  }

  .info-strip {
    position: absolute;
    left: 0; top: 283px;
    width: 586px; height: 57px;
    background: var(--strip);
  }
  .licence, .region {
    position: absolute;
    left: 41px;
    color: var(--white);
    font-size: 14.5px;
    font-weight: 700;
  }
  .licence { top: 289px; }
  .region { top: 314px; }
  .contact { position: absolute; left: 298px; display: flex; align-items: center; color: var(--white); font-weight: 700; white-space: nowrap; }
  .contact svg { width: 20px; height: 20px; margin-right: 9px; flex: none; }
  .contact--phone { top: 287px; font-size: 19px; letter-spacing: 1px; }
  .contact--email { top: 317px; font-size: 12.5px; }

  /* Back */
  .services-panel {
    position: absolute;
    left: 0; top: 0;
    width: 586px; height: 286px;
    background: var(--white);
    border-radius: 72px 72px 0 0;
  }
  .services-title {
    position: absolute;
    left: 0; right: 0; top: 44px;
    text-align: center;
    color: var(--muted-olive);
    font-size: 31px;
    font-weight: 700;
    letter-spacing: 3px;
  }
  .service-list { position: absolute; top: 104px; list-style: none; }
  .service-list li {
    height: 41.5px;
    color: var(--ink);
    font-size: 19px;
    font-weight: 700;
    white-space: nowrap;
  }
  .service-list li::before { content: "\2022"; margin-right: 3px; }
  .service-list--left { left: 42px; }
  .service-list--right { left: 288px; }
  .service-divider {
    position: absolute;
    left: 262px; top: 108px;
    width: 3px; height: 146px;
    background: var(--muted-olive);
  }
  .tagline {
    position: absolute;
    left: 0; width: 560px; top: 286px;
    text-align: center;
    font-family: "Kaushan Script", cursive;
    font-size: 42px;
    color: var(--fluro);
    text-shadow: 0 0 8px rgba(210,242,12,0.7);
    transform: rotate(-2deg);
  }

  .side-label {
    position: absolute;
    left: 792px;
    font-family: "Oswald", sans-serif;
    font-weight: 700;
    font-size: 28px;
    color: var(--label);
    text-shadow: 2px 2px 2px rgba(0,0,0,0.7);
  }
  .side-label--front { top: 470px; }
  .side-label--back { top: 935px; }
</style>
</head>
<body>

<section class="card card--front" aria-label="Card front">
  <svg class="card-art" width="586" height="351" viewBox="0 0 586 351">
    <defs>
      <radialGradient id="glow-right" cx="0.75" cy="0.55" r="0.6">
        <stop offset="0" stop-color="#b9e010"/>
        <stop offset="0.55" stop-color="#4e6a05"/>
        <stop offset="1" stop-color="#050505"/>
      </radialGradient>
      <radialGradient id="glow-bottom" cx="0.3" cy="0.85" r="0.55">
        <stop offset="0" stop-color="#6f9008"/>
        <stop offset="1" stop-color="#050505" stop-opacity="0"/>
      </radialGradient>
      <radialGradient id="bolt-haze" cx="0.5" cy="0.4" r="0.5">
        <stop offset="0" stop-color="#6a6a6a" stop-opacity="0.5"/>
        <stop offset="1" stop-color="#050505" stop-opacity="0"/>
      </radialGradient>
    </defs>
    <rect width="586" height="351" fill="url(#glow-right)" role="img" aria-label="Green lightning and smoke artwork"/>
    <rect width="586" height="351" fill="url(#glow-bottom)"/>
    <path d="M0 0 H544 C544 120 470 196 380 200 H0 Z" fill="#050505"/>
    <path d="M0 200 H380 L300 240 H0 Z" fill="#050505" opacity="0.6"/>
    <path d="M541 0 H560 C558 132 486 202 392 202 C480 190 536 120 541 0 Z" fill="#ffffff"/>
    <rect x="20" y="10" width="140" height="190" fill="url(#bolt-haze)" role="img" aria-label="White lightning bolt artwork"/>
  </svg>

  <div class="brand">
    <span class="brand-dot"></span>
    <h1 class="brand-name">Dorvel Electrical<br>Solutions</h1>
  </div>

  <div class="name-band"></div>
  <p class="person-name">Owen Platt</p>

  <div class="info-strip"></div>
  <p class="licence">Lic No 58342</p>
  <p class="region">Servicing CQ Region</p>

  <p class="contact contact--phone">
    <svg viewBox="0 0 20 20" aria-hidden="true"><circle cx="10" cy="10" r="8.5" fill="none" stroke="#fff" stroke-width="1.5"/><path d="M7 5.5 l1.6 2.4 -1 1.1 c.7 1.5 1.8 2.6 3.3 3.3 l1.1-1 2.4 1.6 -.9 1.6 c-3.8-.3-7-3.5-7.3-7.3 Z" fill="#fff"/></svg>
    0438516274
  </p>
  <p class="contact contact--email">
    <svg viewBox="0 0 20 20" aria-hidden="true"><rect x="2" y="2" width="16" height="16" rx="2" fill="none" stroke="#fff" stroke-width="1.5"/><path d="M5 8 h10 v6 h-10 Z M5 8 l5 3.5 5-3.5" fill="none" stroke="#fff" stroke-width="1.3"/></svg>
    admin@dorvelelectrical.example
  </p>
</section>

<section class="card card--back" aria-label="Card back">
  <svg class="card-art" width="586" height="351" viewBox="0 0 586 351">
    <defs>
      <linearGradient id="band-glow" x1="0" y1="0" x2="1" y2="0">
        <stop offset="0" stop-color="#050505"/>
        <stop offset="0.6" stop-color="#2a3a02"/>
        <stop offset="1" stop-color="#8fb80a"/>
      </linearGradient>
    </defs>
    <rect y="286" width="586" height="65" fill="url(#band-glow)" role="img" aria-label="Green lightning artwork"/>
  </svg>

  <div class="services-panel">
    <h2 class="services-title">Services:</h2>
    <ul class="service-list service-list--left">
      <li>Light &amp; Power</li>
      <li>TV &amp; Data</li>
      <li>Test &amp; Tagging</li>
      <li>Residential</li>
    </ul>
    <div class="service-divider"></div>
    <ul class="service-list service-list--right">
      <li>Renovations</li>
      <li>Design &amp; Installation</li>
      <li>Air Con Installation</li>
      <li>Smoke Detectors</li>
    </ul>
  </div>

  <p class="tagline">Lightning Up CQ!</p>
</section>

<p class="side-label side-label--front">FRONT</p>
<p class="side-label side-label--back">BACK</p>

</body>
</html>
```